Marketing One-Sheet for Security Deposit Claim Notice

I need a one-sheet flyer formatted for email distribution — optimized as a JPEG/PNG that I can insert into Constant Contact or Outlook. I do not want to attach it to an email, but insert it in the email we send out. I would like it to look professional but engaging. Some images would be good, but want to make sure it reads well if images do not load for the recipients. The text is in the attached Word document, but I am open to changes/ideas that may be better for marketing purposes. I included the URLs for some of the links I would like in the one-sheet that is clickable. The logo for the business is being uploaded on the Word document. Proposed text is also uploaded in a Word document. Thank you.

Target Market(s)

Landlords, Real Estate Agents, Property Managers

Industry/Entity Type

Legal

Requirements
Must have
• Professional but appealing design. The One-sheet is going to be placed in the body of emails, not as an attachment.
Nice to have
• Include our logo for the business and the web links please.
Should not have
• Images can be ok, but it needs to look right if images do not download from the email sent out.

```html
<!DOCTYPE html>
<html lang="en">
<head>
<meta charset="utf-8">
<title>Security Deposit Claim Notice</title>
<link rel="stylesheet" href="https://fonts.googleapis.com/css2?family=Gelasio:wght@400;700&family=Karla:wght@400;500&family=Arimo:wght@400;700&family=Tinos&display=swap">
<style>
  :root{
    --backdrop:#e8dcdc;
    --sheet:#ffffff;
    --brand:#8b1520;
    --brand-deep:#7a0010;
    --ink:#1a1a1a;
    --rule:#e6e1e1;
    --tile-rose:#c9a4a8;
    --tile-blush:#efe3e3;
  }
  *{box-sizing:border-box;margin:0;padding:0}
  html,body{width:1200px;height:899px;overflow:hidden}
  body{background:var(--backdrop);position:relative;font-family:"Karla",Arial,sans-serif;color:var(--ink)}
  .sheet{position:absolute;left:351px;top:35px;width:497px;height:829px;background:var(--sheet);box-shadow:0 2px 10px rgba(120,80,80,.12)}
  .brand{position:absolute;left:0;right:0;top:16px;text-align:center;color:var(--brand);font-family:"Gelasio",Georgia,serif}
  .brand-row{display:flex;justify-content:center;align-items:center;gap:8px}
  .brand-name{font-size:22px;line-height:1;letter-spacing:.5px}
  .brand-square{width:22px;height:22px;background:var(--brand)}
  .brand-tagline{font-family:"Karla",Arial,sans-serif;font-size:7px;line-height:1.2;margin-top:5px}
  .brand-contact{font-family:"Karla",Arial,sans-serif;font-size:11px;font-weight:500;line-height:1.3;margin-top:3px}
  .rule{position:absolute;left:30px;right:30px;height:1px;background:var(--rule)}
  .rule.top{top:110px}
  .rule.bottom{top:725px}
  .headline{position:absolute;left:28px;top:132px;width:450px;font-family:"Gelasio",Georgia,serif;font-weight:400;font-size:50px;line-height:50px;color:var(--brand)}
  .body-copy{font-size:10.2px;line-height:14px}
  .intro{position:absolute;left:28px;top:331px;width:440px}
  .col-text{position:absolute;left:28px;width:192px}
  .col-text.first{top:386px}
  .col-text.second{top:484px}
  .price{position:absolute;left:263px;top:395px;width:203px;height:212px;background:var(--brand-deep);border-radius:8px;color:#fff;text-align:center}
  .price-label{font-family:"Arimo",Arial,sans-serif;font-size:17px;margin-top:26px;letter-spacing:.5px}
  .price-main{font-family:"Arimo",Arial,sans-serif;font-size:68px;line-height:1;margin-top:8px}
  .price-alt{font-family:"Arimo",Arial,sans-serif;font-weight:700;font-size:18px;margin-top:18px}
  .price-note{font-family:"Tinos","Times New Roman",serif;font-size:9.5px;letter-spacing:.4px;margin-top:5px}
  .tiles{position:absolute;left:30px;top:627px;width:437px;display:flex;justify-content:space-between}
  .tile{width:100px;height:61px;border-radius:6px;background:var(--tile-rose);color:#fff;font-family:"Tinos","Times New Roman",serif;font-size:18px;display:flex;align-items:center;justify-content:center}
  .tile.light{background:var(--tile-blush)}
  .features{position:absolute;left:28px;top:752px;width:440px;display:flex}
  .feature{flex:1;font-family:"Tinos","Times New Roman",serif;font-size:14.5px;line-height:16.5px;padding-right:20px}
  .feature+.feature{border-left:1px solid var(--rule);padding-left:24px}
</style>
</head>
<body>
  <main class="sheet">
    <header class="brand">
      <div class="brand-row"><span class="brand-name">Tenancy Counsel Group</span><span class="brand-square"></span></div>
      <p class="brand-tagline">a Legal Resource for Landlords,<br>Investors &amp; Property Managers</p>
      <p class="brand-contact">TenancyCounselGroup.com<br>1(800) 555-0142</p>
    </header>
    <div class="rule top"></div>
    <h1 class="headline">Security Deposit Claim Notice- Protect your rights as a Landlord</h1>
    <p class="body-copy intro">Velit ea occaecat nisi consectetur. Ad non pariatur nulla proident officia do proident in. Ut reprehenderit laboris aliquip ex cupidatat qui reprehenderit adipisicing eiusmod tempor enim minim ex cillum. Fugiat non ipsum qui ut laboris.</p>
    <p class="body-copy col-text first">Velit ea occaecat nisi consectetur. Ad non pariatur nulla proident officia do proident in. Ut reprehenderit laboris aliquip ex cupidatat qui reprehenderit adipisicing eiusmod tempor enim minim ex cillum. Fugiat non ipsum qui ut laboris.</p>
    <p class="body-copy col-text second">Velit ea occaecat nisi consectetur. Ad non pariatur nulla proident officia do proident in. Ut reprehenderit laboris aliquip ex cupidatat qui reprehenderit adipisicing eiusmod tempor enim minim ex cillum. Fugiat non ipsum qui ut laboris.</p>
    <section class="price">
      <p class="price-label">FLAT FEE</p>
      <p class="price-main">$350</p>
      <p class="price-alt">$450</p>
      <p class="price-note">COMMERCIAL PROPERTIES</p>
    </section>
    <nav class="tiles">
      <span class="tile">LOREM</span>
      <span class="tile light">LOREM</span>
      <span class="tile">LOREM</span>
      <span class="tile">LOREM</span>
    </nav>
    <div class="rule bottom"></div>
    <footer class="features">
      <p class="feature">Culpa ad tempor aliquip ex commodo.</p>
      <p class="feature">Culpa ad tempor aliquip ex commodo.</p>
      <p class="feature">Culpa ad tempor aliquip ex commodo.</p>
    </footer>
  </main>
</body>
</html>
```